Larkspur Ridge Management - Business Cards

I need business cards. My current logo was designed by a designer at this site and I very much like and am happy with the results. I would like a business card that is trendy, unique, current yet professional. I deal with high net worth clients daily

Target Market(s)

Out of state investors looking to get into the rental market in Ohio

Industry/Entity Type

Property Management, Consulting

Contact Information for Business Card

Name, Title (Chief Financial Officer) office phone number (555) 817-3094 website address larkridgemgmt.example

Font styles to use
Sans Serif

Colors
0054AA
0677BA
7BADD7
CADEEF
E8F1F8
0094D4
00A9DD
6FCCEA
C7EBF8
E9F6FB
00AB8E
00BBA5
67D7C9
C6EFE9
E9F9F6

```html
<!DOCTYPE html>
<html lang="en">
<head>
<meta charset="utf-8">
<title>Larkspur Ridge Management – Business Cards</title>
<link rel="stylesheet" href="https://fonts.googleapis.com/css2?family=Montserrat:wght@400;600;700;800&display=swap">
<style>
  :root {
    --brand-red: #c9202b;
    --brand-navy: #1c2b57;
    --card-white: #f7f7f5;
    --stage: #e9e9e7;
    --ink-soft: #2a2f45;
  }
  * { box-sizing: border-box; margin: 0; padding: 0; }
  html, body {
    width: 1200px;
    height: 800px;
    overflow: hidden;
    background: var(--stage);
    font-family: "Montserrat", sans-serif;
  }
  .sheet {
    position: relative;
    width: 1200px;
    height: 800px;
    display: flex;
    align-items: center;
    justify-content: center;
    gap: 60px;
  }
  .card {
    position: relative;
    width: 520px;
    height: 297px;
    border-radius: 3px;
    overflow: hidden;
    box-shadow: 0 6px 18px rgba(0,0,0,0.14);
  }

  /* Front */
  .card--front { background: var(--brand-navy); }
  .front-band {
    position: absolute;
    left: 0;
    width: 100%;
  }
  .front-band--top { top: 0; height: 55%; background: var(--brand-red); }
  .front-band--bottom { bottom: 0; height: 45%; background: var(--brand-navy); }
  .front-mark {
    position: absolute;
    left: 50%;
    top: 55%;
    transform: translate(-50%, -50%);
    display: flex;
    align-items: center;
    gap: 12px;
    padding: 16px 22px;
    background: var(--brand-navy);
    border-radius: 4px;
  }
  .front-mark__dot {
    width: 14px;
    height: 14px;
    border-radius: 50%;
    background: var(--brand-red);
    flex: none;
  }
  .front-mark__name {
    color: #ffffff;
    font-weight: 800;
    font-size: 19px;
    line-height: 1.15;
    letter-spacing: 0.02em;
    text-transform: uppercase;
  }

  /* Back */
  .card--back { background: var(--card-white); }
  .back-mark {
    position: absolute;
    left: 38px;
    top: 50%;
    transform: translateY(-50%);
    width: 172px;
    color: var(--brand-navy);
    font-weight: 800;
    font-size: 20px;
    line-height: 1.15;
    text-transform: uppercase;
    letter-spacing: 0.02em;
    text-align: center;
  }
  .back-divider {
    position: absolute;
    left: 236px;
    top: 70px;
    width: 2px;
    height: 160px;
    background: var(--brand-navy);
  }
  .contact {
    position: absolute;
    left: 262px;
    top: 84px;
    right: 18px;
  }
  .contact__company {
    color: var(--brand-red);
    font-weight: 700;
    font-size: 15px;
    line-height: 1.2;
  }
  .contact__title {
    color: var(--brand-navy);
    font-weight: 600;
    font-size: 13px;
    margin-top: 3px;
    margin-bottom: 10px;
  }
  .contact__list { list-style: none; }
  .contact__item {
    display: flex;
    align-items: center;
    gap: 8px;
    color: var(--ink-soft);
    font-size: 12px;
    font-weight: 400;
    margin-top: 6px;
  }
  .contact__icon {
    width: 14px;
    height: 14px;
    flex: none;
  }
</style>
</head>
<body>
<main class="sheet">

  <section class="card card--front" aria-label="Business card front">
    <div class="front-band front-band--top" role="img" aria-label="Red band with faint repeating brand pattern"></div>
    <div class="front-band front-band--bottom" role="img" aria-label="Navy band with faint repeating brand pattern"></div>
    <div class="front-mark">
      <span class="front-mark__dot"></span>
      <span class="front-mark__name">Larkspur Ridge<br>Management</span>
    </div>
  </section>

  <section class="card card--back" aria-label="Business card back">
    <div class="back-mark">Larkspur Ridge<br>Management</div>
    <div class="back-divider"></div>
    <div class="contact">
      <p class="contact__company">Larkspur Ridge Management</p>
      <p class="contact__title">Chief Financial Officer</p>
      <ul class="contact__list">
        <li class="contact__item">
          <svg class="contact__icon" viewBox="0 0 14 14" aria-hidden="true">
            <circle cx="7" cy="7" r="7" fill="var(--brand-red)"/>
            <path d="M4.6 3.8c.4-.3.8-.2 1 .2l.5 1c.1.3 0 .6-.2.8l-.4.3c.4.9 1.1 1.6 2 2l.3-.4c.2-.2.5-.3.8-.2l1 .5c.4.2.5.6.2 1l-.4.5c-.4.4-1 .5-1.5.3C6.2 9.1 4.9 7.8 4.2 6.1c-.2-.5-.1-1.1.3-1.5z" fill="#fff"/>
          </svg>
          <span>(555) 817-3094 (Office)</span>
        </li>
        <li class="contact__item">
          <svg class="contact__icon" viewBox="0 0 14 14" aria-hidden="true">
            <circle cx="7" cy="7" r="7" fill="var(--brand-red)"/>
            <rect x="3.8" y="4.8" width="6.4" height="4.4" rx="0.5" fill="#fff"/>
            <path d="M3.9 5l3.1 2.3L10.1 5" fill="none" stroke="var(--brand-red)" stroke-width="0.7"/>
          </svg>
          <span>info@larkridgemgmt.example</span>
        </li>
        <li class="contact__item">
          <svg class="contact__icon" viewBox="0 0 14 14" aria-hidden="true">
            <circle cx="7" cy="7" r="7" fill="var(--brand-red)"/>
            <g fill="none" stroke="#fff" stroke-width="0.8">
              <circle cx="7" cy="7" r="3.3"/>
              <ellipse cx="7" cy="7" rx="1.4" ry="3.3"/>
              <path d="M3.7 7h6.6"/>
            </g>
          </svg>
          <span>larkridgemgmt.example</span>
        </li>
      </ul>
    </div>
  </section>

</main>
</body>
</html>
```